Business Card - Harlow Birch

Need Business Card design for company named Harlow Birch. Software development focused mainly on Ardel eKallo & oBix Apps. I've attached our logo with both a black and white background. Please add trademark symbol to logo when using.

```html
<!DOCTYPE html>
<html lang="en">
<head>
<meta charset="utf-8">
<title>Harlow Birch – Business Cards</title>
<link rel="stylesheet" href="https://fonts.googleapis.com/css2?family=Open+Sans:wght@400;600;700&display=swap">
<style>
  :root {
    --backdrop: #e9e4dc;
    --card-black: #0b0b0b;
    --ink-white: #ffffff;
    --ink-grey: #cfcfcf;
    --ink-muted: #9a9a9a;
    --accent-orange: #f5a623;
    --accent-yellow: #fdb913;
    --accent-red: #e3242b;
    --divider: #555555;
  }
  html, body {
    margin: 0;
    padding: 0;
    width: 1200px;
    height: 720px;
    overflow: hidden;
    background: var(--backdrop);
    font-family: "Open Sans", Arial, sans-serif;
  }
  .canvas {
    position: relative;
    width: 1200px;
    height: 720px;
  }
  .card {
    position: absolute;
    top: 205px;
    width: 540px;
    height: 309px;
    background: var(--card-black);
    overflow: hidden;
    box-shadow: 0 6px 18px rgba(0,0,0,0.18);
  }
  .card--front { left: 40px; }
  .card--back { left: 620px; }

  /* Front */
  .brand {
    position: absolute;
    left: 40px;
    top: 118px;
    display: flex;
    align-items: center;
    gap: 10px;
  }
  .brand__square {
    width: 22px;
    height: 22px;
    background: var(--accent-orange);
  }
  .brand__name {
    color: var(--ink-white);
    font-weight: 700;
    font-size: 24px;
    letter-spacing: -0.5px;
    white-space: nowrap;
  }
  .divider {
    position: absolute;
    left: 262px;
    top: 58px;
    width: 1px;
    height: 130px;
    background: linear-gradient(to bottom, transparent, var(--divider), transparent);
    transform: rotate(-8deg);
  }
  .contact {
    position: absolute;
    left: 292px;
    top: 48px;
    color: var(--ink-grey);
    font-size: 13px;
    line-height: 1.5;
  }
  .contact__name {
    color: var(--accent-orange);
    font-weight: 700;
    font-size: 17px;
    margin: 0;
  }
  .contact__title {
    margin: 0 0 8px;
    font-size: 12px;
    color: var(--ink-grey);
  }
  .contact__line {
    display: flex;
    align-items: center;
    gap: 8px;
    margin: 0;
  }
  .contact__icon { width: 12px; height: 14px; flex: none; }
  .contact__address { margin: 12px 0 0; }
  .bands {
    position: absolute;
    left: 0;
    bottom: 0;
    width: 540px;
    height: 60px;
  }

  /* Back */
  .back-brand {
    position: absolute;
    left: 0;
    right: 0;
    top: 112px;
    text-align: center;
    color: var(--ink-white);
    font-weight: 700;
    font-size: 50px;
    letter-spacing: -1.5px;
    line-height: 1;
  }
  .back-url {
    position: absolute;
    left: 0;
    right: 0;
    top: 200px;
    text-align: center;
    color: var(--ink-grey);
    font-size: 13px;
    letter-spacing: 0.5px;
  }
</style>
</head>
<body>
<main class="canvas">

  <section class="card card--front" aria-label="Business card front">
    <div class="brand">
      <span class="brand__square"></span>
      <span class="brand__name">Harlow Birch™</span>
    </div>

    <span class="divider"></span>

    <div class="contact">
      <p class="contact__name">Your Name</p>
      <p class="contact__title">Title</p>
      <p class="contact__line">
        <svg class="contact__icon" viewBox="0 0 12 14" aria-hidden="true">
          <rect x="2" y="0.5" width="8" height="13" rx="1.5" fill="var(--accent-yellow)"/>
          <rect x="3.5" y="2.5" width="5" height="6" fill="var(--card-black)"/>
          <circle cx="6" cy="11" r="1" fill="var(--card-black)"/>
        </svg>
        555-014-2280
      </p>
      <p class="contact__line">
        <svg class="contact__icon" viewBox="0 0 12 14" aria-hidden="true">
          <path d="M2 12 C1 8 2 4 4 2 L5.5 4.5 L4.5 6 C5 8 6 9 7.5 9.5 L9 8.5 L11.5 10 C10 12 6 13 2 12 Z" fill="var(--accent-yellow)"/>
        </svg>
        555-014-7731
      </p>
      <p class="contact__address">4120 Alder Row, Brookfield, FL 30918</p>
    </div>

    <svg class="bands" viewBox="0 0 540 60" preserveAspectRatio="none" aria-hidden="true">
      <polygon points="0,34 300,34 282,54 0,54" fill="var(--accent-red)"/>
      <polygon points="318,14 540,14 540,34 300,34" fill="var(--accent-yellow)"/>
    </svg>
  </section>

  <section class="card card--back" aria-label="Business card back">
    <div class="back-brand">Harlow Birch™</div>
    <div class="back-url">www.harlowbirch.com</div>
  </section>

</main>
</body>
</html>
```